Bright Orbit Care Re-Design\ Add Hosting Content

We are redesigning our web site. We have already picked out the Kestrel WordPress Hosting theme. All content will come from our current website and go onto the new website. http://www.bright-orbit-care.example . This website will interface with WHMCS billing software. I have attached old logos as well as icons for the hosting theme which is also attached.

Target Market(s)

Tech, Web, Hosting

Industry/Entity Type

Tech

Logo Text

Bright Orbit Care, "The New IT Department"

```html
<!DOCTYPE html>
<html lang="en">
<head>
<meta charset="utf-8">
<title>Bright Orbit Care — The New IT Department</title>
<link rel="stylesheet" href="https://fonts.googleapis.com/css2?family=Raleway:wght@400;500;600;700&family=Open+Sans:wght@400;600&display=swap">
<style>
:root{
  --navy:#1b1580;
  --navy-deep:#140f63;
  --navy-dark:#0e0b4a;
  --icon-navy:#17107a;
  --red:#e2001a;
  --blue:#3a9fea;
  --grey-bg:#ececec;
  --text:#333;
  --muted:#777;
  --link-red:#d4141f;
  --footer-link:#9fa3e6;
  --white:#fff;
}
*{margin:0;padding:0;box-sizing:border-box}
html,body{width:1200px;height:2639px;overflow:hidden;background:var(--white)}
body{position:relative;font-family:"Open Sans",Arial,sans-serif;color:var(--text)}
.abs{position:absolute}
h1,h2,h3,h4,.raleway{font-family:"Raleway","Helvetica Neue",sans-serif;font-weight:500}

/* header */
.site-header{position:absolute;left:0;top:0;width:1200px;height:105px;background:var(--white)}
.brand{position:absolute;left:182px;top:26px;display:flex;align-items:center;gap:12px}
.brand-dot{width:46px;height:46px;border-radius:50%;background:var(--navy)}
.brand-name{font-family:"Raleway",sans-serif;font-weight:700;font-size:22px;color:var(--navy);line-height:1.1}
.brand-tag{font-family:"Raleway",sans-serif;font-weight:700;font-size:14px;color:var(--navy)}
.main-nav{position:absolute;left:546px;top:0;height:105px;display:flex}
.main-nav a{display:flex;align-items:center;padding:0 20px;height:105px;font-family:"Raleway",sans-serif;font-size:14px;color:#222;text-decoration:none;border-right:1px solid #e2e2e2}
.main-nav a:last-child{border-right:none}

/* hero */
.hero{position:absolute;left:0;top:105px;width:1200px;height:486px;background:linear-gradient(100deg,#2c3b55 0%,#6b7f9a 35%,#8a8478 60%,#4a5670 100%)}
.hero h1{position:absolute;left:0;width:1200px;top:176px;text-align:center;color:var(--white);font-size:39px;font-weight:600;line-height:46px;letter-spacing:.5px;text-shadow:0 2px 6px rgba(0,0,0,.4)}
.hero-dots{position:absolute;left:552px;top:447px;display:flex;gap:7px}
.hero-dots span{width:19px;height:19px;border-radius:50%;background:var(--white)}

/* features */
.features{position:absolute;left:0;top:591px;width:1200px;height:219px}
.feature{position:absolute;top:72px;width:270px;display:flex;gap:14px}
.feature-icon{flex:0 0 63px;height:63px;border-radius:50%;background:var(--icon-navy);display:flex;align-items:center;justify-content:center}
.feature h3{font-size:17px;color:var(--icon-navy);margin-top:-2px;margin-bottom:6px}
.feature p{font-size:10px;line-height:17px;color:#666}

/* about */
.about{position:absolute;left:0;top:810px;width:1200px;height:378px;background:var(--grey-bg);border-top:1px solid #ddd}
.about-photo{position:absolute;left:528px;top:0;width:672px;height:378px;background:linear-gradient(90deg,rgba(236,236,236,1) 0%,#cfd6de 25%,#9eabbb 60%,#c8ccd4 100%)}
.about h2{position:absolute;left:191px;top:72px;width:480px;font-size:23px;line-height:34px;color:#222}
.about .copy{position:absolute;left:195px;top:152px;width:410px;font-size:10px;line-height:17px;color:#555}
.about .copy p{margin-bottom:9px}
.btn-red{position:absolute;left:195px;top:257px;width:96px;height:30px;background:var(--red);color:var(--white);font-family:"Raleway",sans-serif;font-weight:700;font-size:11px;display:flex;align-items:center;justify-content:center;border-radius:2px}

/* services */
.services{position:absolute;left:0;top:1188px;width:1200px;height:405px;background:linear-gradient(160deg,#1d2a4e 0%,#0f1a3a 50%,#1c2748 100%)}
.services h2{position:absolute;left:0;width:1200px;top:56px;text-align:center;color:var(--white);font-size:25px}
.service{position:absolute;top:144px;width:220px;text-align:center;color:var(--white)}
.service-icon{width:102px;height:102px;margin:0 auto 18px;border-radius:50%;background:var(--white);display:flex;align-items:center;justify-content:center}
.service h3{font-size:14px;font-weight:600;margin-bottom:4px}
.service p{font-size:10px;line-height:17px;color:#d8dbe6}

/* consult */
.consult{position:absolute;left:0;top:1593px;width:1200px;height:278px;background:linear-gradient(90deg,#3a9fea 0%,#3399e6 50%,#46a8ee 100%)}
.consult h2{position:absolute;left:0;width:1200px;top:37px;text-align:center;color:var(--white);font-size:25px}
.field{position:absolute;height:30px;background:var(--white);border:1px solid #cfd8e0;font-size:10px;color:#888;padding:8px 12px}
.field.message{height:72px}
.btn-submit{position:absolute;left:537px;top:213px;width:137px;height:35px;background:var(--navy-dark);color:var(--white);font-family:"Raleway",sans-serif;font-weight:600;font-size:13px;display:flex;align-items:center;justify-content:center}

/* testimonials & news */
.voices{position:absolute;left:0;top:1871px;width:1200px;height:364px}
.voices h2{position:absolute;top:72px;font-size:22px;color:#222}
.quote-box{position:absolute;left:183px;top:125px;width:418px;height:120px;background:#efefef;border:1px solid #ddd;padding:16px 20px 0 42px;font-size:10px;line-height:18px;color:#666}
.quote-mark{position:absolute;left:14px;top:14px}
.client{position:absolute;left:190px;top:247px;display:flex;align-items:center;gap:14px}
.client-avatar{width:52px;height:52px;border-radius:50%;background:linear-gradient(#cfc8c0,#8d8680);border:2px solid #fff;box-shadow:0 0 0 1px #ccc}
.client-name{font-size:12px;color:#333}
.client-loc{font-size:10px;color:#888}
.news-list{position:absolute;left:645px;top:133px;width:360px}
.news-item{margin-bottom:16px}
.news-item h4{font-family:"Open Sans",sans-serif;font-size:14px;font-weight:400;color:var(--link-red);margin-bottom:6px}
.news-item p{font-size:10px;line-height:18px;color:#666;margin-bottom:8px}
.news-item .date{font-size:10px;color:#555}

/* contact strip */
.contact-strip{position:absolute;left:0;top:2235px;width:1200px;height:72px;background:var(--red);display:flex}
.contact-strip div{display:flex;align-items:center;justify-content:center;gap:12px;color:var(--white);font-family:"Raleway",sans-serif;font-size:21px;border-right:1px solid rgba(255,255,255,.3)}
.contact-strip div:last-child{border-right:none}

/* footer */
.site-footer{position:absolute;left:0;top:2307px;width:1200px;height:277px;background:linear-gradient(180deg,var(--navy) 0%,#1a1277 100%)}
.footer-col{position:absolute;top:58px}
.footer-col h4{font-size:20px;color:var(--white);margin-bottom:14px}
.footer-col a{display:block;font-size:11px;line-height:26px;color:var(--footer-link);text-decoration:none}
.footer-col.info a{color:#c3c6f0}
.badges{display:flex;gap:6px;margin-top:14px}
.badge{width:100px;height:46px;background:#f2f2f2;border-radius:3px}
.badge.dark{background:#2a4e8a}
.bottom-bar{position:absolute;left:0;top:2584px;width:1200px;height:55px;background:var(--navy-deep);font-size:10px;color:#b4b7e8}
.bottom-bar span{position:absolute;left:191px;top:21px}
</style>
</head>
<body>

<header class="site-header">
  <div class="brand">
    <div class="brand-dot"></div>
    <div>
      <div class="brand-name">Bright Orbit Care</div>
      <div class="brand-tag">"The New IT Department"</div>
    </div>
  </div>
  <nav class="main-nav">
    <a href="#">Services</a><a href="#">Business Users</a><a href="#">Home Users</a><a href="#">About</a><a href="#">Contact</a>
  </nav>
</header>

<section class="hero" role="img" aria-label="Photo of a technician helping colleagues at laptops in a bright office">
  <h1>BRIGHT ORBIT CARE NOW OFFERS<br>ON-LINE ORDERING</h1>
  <div class="hero-dots"><span></span><span></span><span></span><span></span></div>
</section>

<section class="features">
  <div class="feature" style="left:193px">
    <div class="feature-icon"><svg width="30" height="30" viewBox="0 0 24 24" fill="#fff"><path d="M21 6.5a5 5 0 0 1-6.6 4.7L6 19.6a1.8 1.8 0 0 1-2.6-2.6l8.4-8.4A5 5 0 0 1 17.5 2l-3 3 .6 2.9 2.9.6z"/></svg></div>
    <div><h3>$50 Flat Rate Repair</h3><p>Morbi eget arcu Morbi porta libero id ullamcorper nonummy nibh ligula pulvinar metus eget consectetuer augue nisi</p></div>
  </div>
  <div class="feature" style="left:484px">
    <div class="feature-icon"><svg width="30" height="30" viewBox="0 0 24 24"><circle cx="12" cy="12" r="10" fill="#fff"/><path d="M7 6c2 1 3 3 2 5s1 3 2 4-1 4-1 5M14 4c0 2 2 2 3 3s-1 3 1 4 2 2 2 3" stroke="#17107a" stroke-width="2" fill="none"/></svg></div>
    <div><h3>Online Backup</h3><p>Morbi eget arcu Morbi porta libero id ullamcorper nonummy nibh ligula pulvinar metus eget consectetu nisi</p></div>
  </div>
  <div class="feature" style="left:757px">
    <div class="feature-icon"><svg width="28" height="28" viewBox="0 0 24 24" fill="#fff"><path d="M2 5h20v14H2z"/><path d="M2 5l10 8 10-8" stroke="#17107a" stroke-width="2" fill="none"/></svg></div>
    <div><h3>Email Solutions</h3><p>Morbi eget arcu Morbi porta libero id ullamcorper nonummy nibh ligula pulvinar metus eget consectetuer augue nisi</p></div>
  </div>
</section>

<section class="about">
  <div class="about-photo" role="img" aria-label="Photo of a smiling support team with headsets at a desk with a laptop"></div>
  <h2>Bright Orbit Care Is The IT Support Solution To Your Business &amp; Home Needs!</h2>
  <div class="copy">
    <p>Curabitur iaculis tempus eros Curabitur vel mi sit amet magna malesuada ultrices Ut nisi erat fermentum vel congue id euismod in elit Fusce ultricies orci ac feugiat suscipit leo massa sodales velit et scelerisque mi tortor at ipsum cligula augue</p>
    <p>bibendum accumsan vestibulum ut commodo a mi Morbi ornare gravida elit Integer congue augue et malesuada iaculis ipsum dui aliquet felis at cursus</p>
  </div>
  <div class="btn-red">READ MORE</div>
</section>

<section class="services" role="img" aria-label="Dark blue photo of hands working on computer hardware">
  <h2>Services Provides</h2>
  <div class="service" style="left:163px">
    <div class="service-icon"><svg width="42" height="42" viewBox="0 0 24 24" fill="none" stroke="#17107a" stroke-width="2.4"><path d="M4 12a8 8 0 1 0 2.5-5.8"/><path d="M3 3v5h5" /><path d="M12 8v4l3 2"/></svg></div>
    <h3>Data Backup &amp; Recovery</h3><p>Morbi eget arcu Morbi porta libero id ullamcorper nonummy nibh</p>
  </div>
  <div class="service" style="left:376px">
    <div class="service-icon"><svg width="40" height="40" viewBox="0 0 24 24" fill="#17107a"><path d="M11 2a10 10 0 1 0 11 11H11z"/><path d="M13 0a10 10 0 0 1 10 10H13z" transform="translate(0 1)"/></svg></div>
    <h3>Repair &amp; Diagnotics</h3><p>Morbi eget arcu Morbi porta libero id ullamcorper nonummy nibh</p>
  </div>
  <div class="service" style="left:590px">
    <div class="service-icon"><svg width="40" height="40" viewBox="0 0 24 24" fill="#17107a"><path d="M10 2h4v8h4l-6 7-6-7h4z"/><path d="M2 16h5l2 3h6l2-3h5v6H2z"/></svg></div>
    <h3>Update &amp; Instllation</h3><p>Morbi eget arcu Morbi porta libero id ullamcorper nonummy nibh</p>
  </div>
  <div class="service" style="left:802px">
    <div class="service-icon"><svg width="42" height="42" viewBox="0 0 24 24" fill="#17107a"><path d="M2 3h20v14H2z"/><path d="M4 5h16v10H4z" fill="#fff"/><path d="M9 17h6v3h3v2H6v-2h3z"/></svg></div>
    <h3>Computer Networking</h3><p>Morbi eget arcu Morbi porta libero id ullamcorper nonummy nibh</p>
  </div>
</section>

<section class="consult">
  <h2>Free Consultations Now</h2>
  <div class="field" style="left:290px;top:88px;width:201px">Your name</div>
  <div class="field" style="left:502px;top:88px;width:200px">Email address</div>
  <div class="field" style="left:711px;top:88px;width:201px">Phone no.</div>
  <div class="field message" style="left:290px;top:127px;width:622px">Message</div>
  <div class="btn-submit">SUBMIT NOW</div>
</section>

<section class="voices">
  <h2 style="left:183px">What Our Clients Say</h2>
  <div class="quote-box">
    <svg class="quote-mark" width="22" height="16" viewBox="0 0 22 16" fill="#e2001a"><path d="M0 8q0-7 8-8v3q-4 1-4 4h4v9H0zM12 8q0-7 8-8v3q-4 1-4 4h4v9h-8z"/></svg>
    Massa libero interdum nec interdum vel blandit sed nulla in ullamcorper est eget tempor cursus neque mi consectetuer mi a ultricies massa est sed nisl Class aptent taciti sociosqu ad litora torquent per conubia nostra per inceptos hymenaeos Proin nulla arcu nonummy luctus dictum
  </div>
  <div class="client">
    <div class="client-avatar" role="img" aria-label="Client portrait"></div>
    <div><div class="client-name">Dana Whitfield</div><div class="client-loc">Location, Post</div></div>
  </div>

  <h2 style="left:643px">Recent News</h2>
  <div class="news-list">
    <div class="news-item">
      <h4>Massa libero interdum nec interdum vel</h4>
      <p>sed nulla in ullamcorper est eget tempor cursus neque mi consectetuer mi a ultricies massa est sed nisl Class aptent taciti sociosqu ad litora</p>
      <div class="date">Posted 2 days ago</div>
    </div>
    <div class="news-item">
      <h4>Cum sociis natoque penatibus et</h4>
      <p>Morbi eget arcu Morbi porta libero id ullamcorper nonummy nibh ligula pulvinar metus eget consectetuer augue nisi quis lacus Ut ac mi quis lacus mollis aliquam Curabitur iaculis tempus</p>
      <div class="date">Posted 2 days ago</div>
    </div>
  </div>
</section>

<section class="contact-strip">
  <div style="width:412px"><svg width="32" height="24" viewBox="0 0 24 18" fill="#fff"><path d="M0 0h24v18H0z"/><path d="M0 0l12 9 12-9" stroke="#e2001a" stroke-width="2" fill="none"/></svg>Email Us</div>
  <div style="width:306px"><svg width="24" height="26" viewBox="0 0 24 24" fill="#fff"><path d="M6.6 10.8a15 15 0 0 0 6.6 6.6l2.2-2.2c.3-.3.7-.4 1-.2 1.1.4 2.3.6 3.6.6.6 0 1 .4 1 1V20c0 .6-.4 1-1 1A17 17 0 0 1 3 4c0-.6.4-1 1-1h3.5c.6 0 1 .4 1 1 0 1.3.2 2.5.6 3.6.1.3 0 .7-.2 1z"/></svg>(555) 014-2276</div>
  <div style="width:482px"><svg width="36" height="28" viewBox="0 0 30 24" fill="none" stroke="#fff" stroke-width="2.2"><path d="M2 9c0-4 4-7 9-7s9 3 9 7-4 7-9 7l-5 3 1-4c-3-1-5-3-5-6z"/><path d="M22 8c3 1 6 3 6 6 0 2-1 3-3 4l1 4-4-3c-3 0-6-1-7-3"/></svg>Live chat with Us</div>
</section>

<footer class="site-footer">
  <div class="footer-col" style="left:199px">
    <h4>Company</h4>
    <a href="#">About Bright Orbit Care</a><a href="#">Our Partners</a><a href="#">Terms &amp; Conditions</a><a href="#">Privacy Policy</a><a href="#">Certifications</a>
  </div>
  <div class="footer-col" style="left:424px">
    <h4>Services</h4>
    <a href="#">Class aptent</a><a href="#">Taciti sociosqu ad</a><a href="#">Litora torquent</a><a href="#">Per conubia nostra</a><a href="#">Aer inceptos</a>
  </div>
  <div class="footer-col" style="left:618px">
    <h4>Resources</h4>
    <a href="#">Testimonials</a><a href="#">News</a><a href="#">Security Alerts</a><a href="#">Contact Us</a><a href="#">Sitemap</a>
  </div>
  <div class="footer-col info" style="left:818px">
    <h4>Contact Info</h4>
    <a>2210 W. Harbor Lane, Ste 4</a><a>Lakeview, Nebraska 60000</a><a>(555) 014-2276</a><a>info@bright-orbit-care.example</a>
    <div class="badges"><div class="badge dark"></div><div class="badge"></div></div>
  </div>
</footer>
<div class="bottom-bar"><span>© 2015 Company Name &nbsp;All right reserved &nbsp;Term of Use</span></div>

</body>
</html>
```